Company Services Brochure - Brightpath Harbor Consulting

I need a brochure detailing our company and making a solid value proposition for what we do and our services. I need it by Tuesday for a big meeting Thursday. The website is www.brightpathharborco.com

The company focuses on partnering with our clients to accomplish big goals and solve challenges through people and strategy. We are certified executive coaches and leadership developers (we train and coach leaders), and we develop and monitor strategic plans and the implementation of the plan. Managing Partner - R. Milton Graves and Senior Parter - Paula Ostrander .... pics are attached....please let me know whatever else you need and I can upload.
Updates

This would be a trifold - front back for our potential clients.... We work in all industries - public, private, government, education, nonprofit, faith based, etc. Please let me know if you have other questions. And, please be creative!!

```html
<!DOCTYPE html>
<html lang="en">
<head>
<meta charset="UTF-8">
<title>Brightpath Harbor Consulting – Services Brochure</title>
<link href="https://fonts.googleapis.com/css2?family=Open+Sans:wght@300;400;600;700;800&display=swap" rel="stylesheet">
<style>
  :root{
    --navy:#1d3566;
    --navy-deep:#142852;
    --navy-bright:#2d5597;
    --accent-blue:#3b6fb6;
    --band-gray:#e4e5e8;
    --band-blue:#d9e3f0;
    --ink:#2b2b2b;
    --paper:#ffffff;
    --backdrop:#f1f1f1;
    --mid-gray:#8a8d93;
  }
  *{box-sizing:border-box;margin:0;padding:0}
  html,body{width:1200px;height:800px;overflow:hidden;background:var(--backdrop)}
  body{font-family:"Open Sans",Arial,sans-serif;color:var(--ink)}
  .brochure{display:flex;width:1200px;height:800px}
  .panel{position:relative;width:400px;height:800px;background:var(--paper);overflow:hidden}
  .panel-bg{position:absolute;inset:0;width:100%;height:100%}
  .panel-content{position:relative;z-index:1}

  /* Panel 1 */
  .intro .panel-content{padding:58px 36px 0 40px}
  .section-title{font-size:25px;letter-spacing:1px;color:var(--navy);font-weight:300}
  .section-title strong{font-weight:800}
  .title-rule{width:22px;height:3px;background:var(--mid-gray);margin:12px 0 16px}
  .body-copy{font-size:12.2px;line-height:1.4;margin-bottom:12px}
  .cycle-diagram{position:absolute;left:0;top:532px;width:400px;height:262px;z-index:1}
  .cycle-diagram text{font-family:"Open Sans",Arial,sans-serif}
  .step-num{font-size:19px;font-weight:700;fill:var(--navy)}
  .step-label{font-size:8px;fill:var(--accent-blue)}
  .phase-label{font-size:8px;fill:var(--mid-gray);font-weight:600;letter-spacing:.5px}
  .center-name{font-size:17px;font-weight:700;fill:var(--navy)}

  /* Panel 2 */
  .process .panel-content{padding:50px 36px 0 34px}
  .checklist{list-style:none;margin-top:20px}
  .checklist li{position:relative;padding-left:20px;font-size:13px;line-height:1.38;margin-bottom:3px}
  .checklist li::before{content:"";position:absolute;left:2px;top:4px;width:6px;height:10px;border:solid var(--accent-blue);border-width:0 2px 2px 0;transform:rotate(45deg)}
  .team-photo{position:absolute;left:0;bottom:0;width:400px;height:250px;background:linear-gradient(180deg,#ffffff 0%,#e6ebf1 25%,#c9d2dc 60%,#8f9fb3 100%)}

  /* Panel 3 */
  .services{background:var(--navy)}
  .portrait-photo{position:absolute;left:0;top:0;width:400px;height:440px;background:radial-gradient(ellipse at 50% 40%,#6b4a38 0%,#3a2519 45%,#1b100b 100%)}
  .services .panel-content{position:absolute;left:34px;top:400px;right:24px}
  .services-title{color:#fff;font-size:24px;font-weight:300;letter-spacing:1px}
  .services-title strong{font-weight:800}
  .services-list{list-style:none;margin-top:16px}
  .services-list li{position:relative;padding-left:18px;color:#fff;font-size:12.4px;line-height:1.4;margin-bottom:3px}
  .services-list li::before{content:"";position:absolute;left:2px;top:3px;width:5px;height:9px;border:solid #9fc0ea;border-width:0 2px 2px 0;transform:rotate(45deg)}
</style>
</head>
<body>
<main class="brochure">

  <!-- Panel 1: Strategic planning -->
  <section class="panel intro">
    <svg class="panel-bg" viewBox="0 0 400 800" preserveAspectRatio="none" aria-hidden="true">
      <path d="M0 250 C120 220 260 200 400 150 L400 300 C260 330 120 350 0 380 Z" fill="var(--band-gray)"/>
      <path d="M0 470 C140 430 260 400 400 350 L400 480 C260 520 140 560 0 600 Z" fill="var(--band-blue)"/>
      <path d="M120 640 C220 600 320 580 400 560 L400 700 C320 680 220 670 120 640 Z" fill="var(--band-blue)" opacity=".6"/>
    </svg>
    <div class="panel-content">
      <h1 class="section-title">STRATEGIC <strong>PLANNING</strong></h1>
      <div class="title-rule"></div>
      <p class="body-copy">The vast majority of organizations operate within the framework of a five-year strategic planning encompassing multiple areas.</p>
      <p class="body-copy">Many entities engage in strategic planning, a structured process designed to produce strategic decisions and actions that shape and guide what an organization is, who it serves, what it does, and why it does with a focus on the future. Strategic planning should be thought of as a necessary element in every organization, and the importance of strategic planning cannot be overstated. Properly designed and implemented, strategic planning is a proactive process of envisioning the future and developing the necessary strategic actions to bring that vision to fruition. Most important, it is a process of defining and setting priorities, focusing energy and resources, building consensus around expected outcomes and results, and ensuring an organization’s staff and stakeholders are working toward a common goal—strategy and making the decisions on allocating its resources, including capital and people to achieve winning outcomes.</p>
    </div>
    <svg class="cycle-diagram" viewBox="0 0 400 270" role="img" aria-label="Six-step strategic planning cycle">
      <defs>
        <marker id="arrowhead" markerWidth="8" markerHeight="8" refX="6" refY="4" orient="auto">
          <path d="M0 0 L8 4 L0 8 Z" fill="var(--mid-gray)"/>
        </marker>
      </defs>
      <polygon points="140,40 250,40 310,135 250,230 140,230 80,135" fill="none" stroke="var(--navy)" stroke-width="6"/>
      <line x1="162" y1="16" x2="225" y2="16" stroke="var(--mid-gray)" stroke-width="1.5" marker-end="url(#arrowhead)"/>
      <text class="phase-label" x="176" y="11">ENGAGE</text>
      <line x1="330" y1="160" x2="306" y2="200" stroke="var(--mid-gray)" stroke-width="1.5" marker-end="url(#arrowhead)"/>
      <text class="phase-label" x="318" y="192">FOCUS</text>
      <line x1="62" y1="208" x2="72" y2="162" stroke="var(--mid-gray)" stroke-width="1.5" marker-end="url(#arrowhead)"/>
      <text class="phase-label" x="34" y="222">EXECUTE</text>

      <g>
        <rect x="123" y="23" width="34" height="34" fill="#fff" stroke="var(--navy)" stroke-width="5"/>
        <text class="step-num" x="140" y="47" text-anchor="middle">1</text>
        <rect x="233" y="23" width="34" height="34" fill="#fff" stroke="var(--navy)" stroke-width="5"/>
        <text class="step-num" x="250" y="47" text-anchor="middle">2</text>
        <rect x="293" y="118" width="34" height="34" fill="#fff" stroke="var(--navy)" stroke-width="5"/>
        <text class="step-num" x="310" y="142" text-anchor="middle">3</text>
        <rect x="233" y="213" width="34" height="34" fill="#fff" stroke="var(--navy)" stroke-width="5"/>
        <text class="step-num" x="250" y="237" text-anchor="middle">4</text>
        <rect x="123" y="213" width="34" height="34" fill="#fff" stroke="var(--navy)" stroke-width="5"/>
        <text class="step-num" x="140" y="237" text-anchor="middle">5</text>
        <rect x="63" y="118" width="34" height="34" fill="#fff" stroke="var(--navy)" stroke-width="5"/>
        <text class="step-num" x="80" y="142" text-anchor="middle">6</text>
      </g>

      <text class="step-label" x="115" y="36" text-anchor="end">Assess &amp;</text>
      <text class="step-label" x="115" y="45" text-anchor="end">Organize</text>
      <text class="step-label" x="272" y="32">Current</text>
      <text class="step-label" x="272" y="41">Reality Scan</text>
      <text class="step-label" x="332" y="132">Strategic</text>
      <text class="step-label" x="332" y="141">Design</text>
      <text class="step-label" x="272" y="232">Strategic</text>
      <text class="step-label" x="272" y="241">Planning</text>
      <text class="step-label" x="116" y="248" text-anchor="end">Strategic</text>
      <text class="step-label" x="116" y="257" text-anchor="end">Implementation</text>
      <text class="step-label" x="56" y="138" text-anchor="end">Monitor</text>

      <text class="center-name" x="196" y="130" text-anchor="middle">Brightpath Harbor</text>
      <text class="center-name" x="196" y="152" text-anchor="middle">Consulting</text>
    </svg>
  </section>

  <!-- Panel 2: Planning process -->
  <section class="panel process">
    <svg class="panel-bg" viewBox="0 0 400 800" preserveAspectRatio="none" aria-hidden="true">
      <path d="M0 90 C140 80 280 70 400 60 L400 140 C280 160 140 170 0 180 Z" fill="var(--band-gray)"/>
      <path d="M0 320 C140 300 280 260 400 230 L400 340 C280 360 140 390 0 420 Z" fill="var(--band-blue)"/>
    </svg>
    <div class="panel-content">
      <p class="body-copy">Strategic planning moves organizations from reactionary modes to proactive modes by assessing and adjusting an organization’s direction in response to a changing environment. Strategic plans not only articulate where an organization is going, but also how it will know if it is successful by connecting goals, strategies, performance measures, and action plans to an overall resource allocation process. To have a successful strategic plan, you need both the strategic plan and a way to measure the progress of strategic plan implementation. Organizations that link these elements through the planning process are much more likely to make decisions that lead to achievement of identified goals and enhance their overall organizational effectiveness. Brightpath Harbor Consulting’s strategic planning process includes the following key elements:</p>
      <ul class="checklist">
        <li>Consensus on Mission, Vision, Values;</li>
        <li>Assessment of strengths and weaknesses, opportunities, and threats;</li>
        <li>Identification of external trends, events, and factors;</li>
        <li>Identification of strategic priorities;</li>
        <li>Goals and objectives with measurable time-framed targets;</li>
        <li>Implementation plan; and</li>
        <li>Monitoring tools.</li>
      </ul>
    </div>
    <div class="team-photo" role="img" aria-label="Photo of a business team meeting around a laptop"></div>
  </section>

  <!-- Panel 3: Services -->
  <section class="panel services">
    <div class="portrait-photo" role="img" aria-label="Portrait photo of a smiling senior partner"></div>
    <svg class="panel-bg" viewBox="0 0 400 800" preserveAspectRatio="none" aria-hidden="true">
      <defs>
        <linearGradient id="navyFade" x1="0" y1="0" x2="1" y2="1">
          <stop offset="0" stop-color="var(--navy-bright)"/>
          <stop offset="1" stop-color="var(--navy-deep)"/>
        </linearGradient>
      </defs>
      <path d="M0 420 C120 360 260 310 400 230 L400 262 C260 340 120 395 0 450 Z" fill="#9a9da3"/>
      <path d="M0 450 C120 395 260 340 400 262 L400 800 L0 800 Z" fill="url(#navyFade)"/>
      <path d="M0 450 C120 395 260 340 400 262" fill="none" stroke="#ffffff" stroke-width="3"/>
    </svg>
    <div class="panel-content">
      <h2 class="services-title">OUR <strong>SERVICES</strong></h2>
      <ul class="services-list">
        <li>Talent &amp; Leadership Development, including Leadership Training &amp; Coaching Services for Mid-Level and Senior Managers as well as Executive Staff</li>
        <li>Organizational Strategic Planning Development, Implementation &amp; Execution, and Monitoring</li>
        <li>Organizational Improvement Support</li>
        <li>Leadership Support</li>
        <li>Equity, Diversity &amp; Inclusion Support including Strategy and Training</li>
        <li>Fundraising &amp; Development Support</li>
        <li>Human Resources Support, including Executive Search Support</li>
        <li>Strategic Advising</li>
        <li>Sales &amp; Marketing</li>
        <li>Communications &amp; Public Relations</li>
      </ul>
    </div>
  </section>

</main>
</body>
</html>
```